Stationery for use with Vellmar reports

I would like to get a stationery design that my firm -- Vellmar Partners -- will use as a format for reports that we send our clients. I am specifically looking for a design for use on a piece of paper or letterhead -- not business cards or envelopes.

We are an Africa based US risk intelligence and strategy firm that works with multinational corporations operating in West Africa. Our initial thinking is that we would like a color scheme consistent with our existing logo -- however we are open to other color schemes.

Also, we would like to see at least two separate versions: one with our company name and logo, the other without name and logo.

We also would like font recommendations for the stationary design.

The final design should communicate discreet professionalism and a modern approach, but it should not overshadow the words and information printed on the stationery.

Target Market(s)

Multinational corporations that currently use our products.

Font styles to use
Serif
Sans Serif

Requirements
Must have
• Sense of discreet professionalism that will not overshadow the content we put onto the stationery format.
• We would like to see designs with and without our company name/logo.
• Please suggest fonts that would work with the stationery.
Nice to have
• Ideally colors consistent with out existing logo, though we are open to and even encourage other ideas.
Should not have
• No need for business cards or envelopes.

```html
<!DOCTYPE html>
<html lang="en">
<head>
<meta charset="utf-8">
<title>Vellmar Partners — Letterhead</title>
<link rel="stylesheet" href="https://fonts.googleapis.com/css2?family=Open+Sans:wght@400;700&display=swap">
<style>
  :root {
    --backdrop: #d3d3d5;
    --paper: #f6f6f6;
    --navy: #1e3846;
    --gold: #d9a245;
    --body-text: #4b4b4b;
    --signature-tone: #e6e6e6;
  }
  * { box-sizing: border-box; margin: 0; padding: 0; }
  html, body {
    width: 1200px;
    height: 1108px;
    overflow: hidden;
    background: var(--backdrop);
  }
  .letterhead {
    position: absolute;
    left: 233px;
    top: 34px;
    width: 734px;
    height: 1040px;
    background: var(--paper);
    font-family: "Open Sans", sans-serif;
    color: var(--body-text);
  }
  .brand {
    position: absolute;
    left: 67px;
    top: 150px;
    display: flex;
    align-items: center;
    gap: 10px;
  }
  .brand-square {
    width: 22px;
    height: 22px;
    background: var(--gold);
  }
  .brand-name {
    font-weight: 700;
    font-size: 24px;
    letter-spacing: -0.3px;
    color: var(--navy);
    line-height: 1;
  }
  .letter-body {
    position: absolute;
    left: 67px;
    top: 282px;
    width: 604px;
    font-size: 13.6px;
    letter-spacing: -0.15px;
    line-height: 20px;
  }
  .salutation { margin-bottom: 20px; }
  .paragraph {
    text-align: justify;
    margin-bottom: 20px;
  }
  .signature {
    display: block;
    margin-top: 16px;
    width: 88px;
    height: 82px;
    background: var(--signature-tone);
  }
</style>
</head>
<body>
  <main class="letterhead">
    <header class="brand">
      <span class="brand-square"></span>
      <span class="brand-name">Vellmar Partners</span>
    </header>

    <section class="letter-body">
      <p class="salutation">Dear customer,</p>
      <p class="paragraph">Lorem ipsum dolor sit amet, consectetur adipisicing elit, sed do eiusmod tempor incididunt ut labore et dolore magna aliqua. Ut enim ad minim veniam, quis nostrud exercitation ullamco laboris nisi ut aliquip ex ea commodo consequat. Duis aute irure dolor in reprehenderit in voluptate velit esse cillum dolore eu fugiat nulla pariatur. Excepteur sint occaecat cupidatat non proident, sunt in culpa qui officia deserunt mollit anim id est laborum.</p>
      <p class="paragraph">Lorem ipsum dolor sit amet, consectetur adipisicing elit, sed do eiusmod tempor incididunt ut labore et dolore magna aliqua. Ut enim ad minim veniam, quis nostrud exercitation ullamco laboris nisi ut aliquip ex ea commodo consequat. Duis aute irure dolor in reprehenderit in voluptate velit esse cillum dolore eu fugiat nulla pariatur. Excepteur sint occaecat cupidatat non proident, sunt in culpa qui officia deserunt mollit anim id est laborum.</p>
      <p class="paragraph">Lorem ipsum dolor sit amet, consectetur adipisicing elit, sed do eiusmod tempor incididunt ut labore et dolore magna aliqua. Ut enim ad minim veniam, quis nostrud exercitation ullamco laboris nisi ut aliquip ex ea commodo consequat. Duis aute irure dolor in reprehenderit in voluptate velit esse cillum dolore eu fugiat nulla pariatur. Excepteur sint occaecat cupidatat non proident, sunt in culpa qui officia deserunt mollit anim id est laborum.</p>
      <p class="paragraph">Lorem ipsum dolor sit amet, consectetur adipisicing elit, sed do eiusmod tempor incididunt ut labore et dolore magna aliqua. Ut enim ad minim veniam, quis nostrud exercitation ullamco laboris nisi ut aliquip ex ea commodo consequat. Duis aute irure dolor in reprehenderit.</p>
      <p class="closing">Yours Sincerely,</p>
      <div class="signature" role="img" aria-label="Handwritten signature of the sender"></div>
    </section>
  </main>
</body>
</html>
```